Holiday Rental Company Flyer Design (DL not A5)

Note from PixelFolk Administration: The category sizing selected is A5, however the project requires DL sized artwork. Please refer to the DL template link below while the 'Special Requirements' are updated accordingly.

Project Brief:
We need a double sided DL flyer designed for an up market Holiday Rental Company that portrays a personalised approach to property management. These are to be used for letter box drops to homes we're specifically targeting so the design should be modern, complimentary colour palette, uncluttered & visually appealing.

Please Download the DL Template from Quillmark here: http://www.quillmark.com.au/qm/ns/propath/UploadResources.aspx?selectedTab=0?pfid=BFB&pf_id=BFB&xnav=easypath-upload-image#Templates

Target Market(s)

Wealthy Home Owners

Industry/Entity Type

It Company

Font styles to use
Other font styles liked:
• Avant Garde Extra Light & Demi

Colors
33b8a4

Requirements
Must have
• DL Flyer sizes (210mm width x 99mm width, plus 3mm bleed)
• Front: Logo, Main Image & Grab
• Back: Contact Details & Brief Description of our business
• Images: Ideally the main image should be the house with the pool but alternatively a lifestyle images could also be used.
Nice to have
• A creative designer!
Should not have
• Clutter & busy designs

```html
<!DOCTYPE html>
<html lang="en">
<head>
<meta charset="utf-8">
<title>Coastline Retreats – DL Flyer</title>
<link rel="stylesheet" href="https://fonts.googleapis.com/css2?family=Questrial&display=swap">
<style>
  :root {
    --page-bg: #000000;
    --teal: #4fae8e;
    --teal-label: #5cc0a0;
    --teal-light: #6cc2a3;
    --teal-deep: #3f9479;
    --ink: #6b6b6b;
    --white: #ffffff;
  }
  * { margin: 0; padding: 0; box-sizing: border-box; }
  html, body {
    width: 1200px; height: 1125px; overflow: hidden;
    background: var(--page-bg);
    font-family: "Questrial", "Century Gothic", sans-serif;
  }
  .sheet { position: relative; width: 1200px; height: 1125px; }

  .side-label {
    position: absolute; left: 0; width: 1200px; text-align: center;
    color: var(--teal-label); font-size: 16px; letter-spacing: 6px;
  }
  .side-label--front { top: 36px; }
  .side-label--back { top: 1080px; }

  /* Front */
  .flyer-front {
    position: absolute; left: 90px; top: 74px; width: 1020px; height: 480px;
    overflow: hidden;
  }
  .hero-image {
    position: absolute; inset: 0;
    background:
      linear-gradient(115deg, transparent 55%, rgba(255,255,255,0.06) 55%, rgba(255,255,255,0.06) 75%, transparent 75%),
      radial-gradient(ellipse at 25% 60%, var(--teal-light) 0%, transparent 55%),
      linear-gradient(180deg, var(--teal-deep) 0%, var(--teal-light) 55%, var(--teal) 100%);
  }
  .brand {
    position: absolute; left: 0; top: 150px; width: 100%; text-align: center;
    color: var(--white);
  }
  .brand__name {
    font-size: 42px; line-height: 44px; letter-spacing: 3px; font-weight: 400;
  }
  .brand__dot {
    display: block; width: 14px; height: 14px; margin: 22px auto 0;
    border: 1.5px solid var(--white); border-radius: 50%;
  }
  .tagline {
    position: absolute; left: 0; bottom: 30px; width: 100%; text-align: center;
    color: var(--white); font-size: 20px; letter-spacing: 0.3px;
  }

  /* Back */
  .flyer-back {
    position: absolute; left: 90px; top: 575px; width: 1020px; height: 481px;
    background: var(--white);
  }
  .about {
    position: absolute; left: 0; top: 38px; width: 100%; text-align: center;
    color: var(--ink); font-size: 14px; line-height: 18px;
  }
  .about__heading {
    color: var(--teal); font-size: 15px; font-weight: 700; margin-bottom: 17px;
  }
  .about p { margin-bottom: 17px; }
  .about .services { margin-bottom: 17px; }
  .contacts {
    display: flex; justify-content: center; gap: 28px;
    color: var(--teal); font-size: 15px; font-weight: 700;
  }
  .gallery {
    position: absolute; left: 0; top: 309px; width: 1020px; height: 172px;
    display: flex;
  }
  .gallery__photo { height: 100%; }
  .photo--bedroom { width: 240px; background: linear-gradient(160deg, #d9b98a 0%, #c9b24a 50%, #e06a5a 100%); }
  .photo--bay { width: 244px; background: linear-gradient(180deg, #c9d6df 0%, #8fb3cc 50%, #6f9fbf 100%); }
  .photo--pool { width: 288px; background: linear-gradient(180deg, #1c1c2e 0%, #4a4870 50%, #3f7fd6 100%); }
  .photo--bathroom { width: 248px; background: linear-gradient(160deg, #d8d6d0 0%, #bdbab3 55%, #9e9b94 100%); }
</style>
</head>
<body>
<main class="sheet">
  <div class="side-label side-label--front">FRONT</div>

  <section class="flyer-front">
    <div class="hero-image" role="img" aria-label="Modern house interior with glass walls, tinted teal"></div>
    <div class="brand">
      <div class="brand__name">COASTLINE<br>RETREATS</div>
      <span class="brand__dot"></span>
    </div>
    <div class="tagline">Holiday Rental Management with a difference</div>
  </section>

  <section class="flyer-back">
    <div class="about">
      <h2 class="about__heading">What we do differently!</h2>
      <p>Rather than relying upon a key safe or a central pick-up destination, a ‘Coastline Retreats’ staff member will greet guests upon arrival.</p>
      <p>Our ‘Meet &amp; Greet’ service provides home owners with an increased level of Security and also allows us to:</p>
      <div class="services">
        Prepare the home for their arrival (lights, heaters, music etc.)<br>
        Establish a rapport &amp; help facilitate future bookings Reiterate their responsibilities to ensure the return of their bond
      </div>
      <p>If you’d like to know what your property could achieve or require additional information, please contact us on:</p>
      <div class="contacts">
        <span>t: (03)5900 1234</span>
        <span>e: stay@coastlineretreats.com.au</span>
        <span>w: coastlineretreats.com.au</span>
        <span>PO Box 12, Seaview Victoria 3999</span>
      </div>
    </div>
    <div class="gallery">
      <div class="gallery__photo photo--bedroom" role="img" aria-label="Bedroom with yellow cushions and colourful bedspread"></div>
      <div class="gallery__photo photo--bay" role="img" aria-label="Sailing boat on a calm bay"></div>
      <div class="gallery__photo photo--pool" role="img" aria-label="Modern house with lit pool at dusk"></div>
      <div class="gallery__photo photo--bathroom" role="img" aria-label="Bathroom basin with flowers"></div>
    </div>
  </section>

  <div class="side-label side-label--back">BACK</div>
</main>
</body>
</html>
```